Velvet Paws Website - Boutique online pet store for both owners, their homes and their dogs

I need a high end online store for the sale of dog products (collars, leashes, coats etc), products for their owners (pyjamas, cosmetic bags, pencil cases, gift wrapping paper, greeting cards etc) and the owners home (ring holders, cushion covers, throws etc).

Please peruse the following website for a vauge idea of slightly similar stores:

Mybeaglecorner.com.au
Pebblepuphaven.com.au
Terrierplace.com.au
Tallhound.co.za

Please keep in mind these are breed specific sites. I intend for the business to sell to trending dog breeds, for example, currently in Australia, French Bulldogs and Dachshunds are trending; therefore this will be the business's current focus.

I also intend for this website to be more elegant and refined than the websites mentioned above. Similar to top names brands, with a hint of cuteness to appeal to the animal lover within customers.

Target Market(s)

Velvet Paws' target market is majority females, late 20's - 40's, either single, in a relationship, or with children who have left the home. They own small and pampered dogs and treat these dogs like their children. They will have a high disposable income.

I want the brand to attract elitist clientele. Comment has been made that people mightn't be able to spell Velvet when searching for the website; those are not the type of customers I want to attract. I think it may be difficult to encapsulate these two target ideas into the brand; I'd like is to appeal to both the 'Melbourne Socialite' and the Noosa stereotype of "I'm too cool to show it, but I really care what you think"

The products will be, for the most part, unique to the market, a few examples include:

custom hand made collars and leads reflecting current human fashion trends;
leather coats for dogs;
flannel pyjamas for dog;
chef's hats for dogs;
furniture which incorporates dogs beds (blanket box, coffee table, bedside table)
bags, cushions, throw rugs, pyjamas made from various dog print fabrics;
fine leather handbags and purses with various and discreet dog themed embellishments;
custom gift wrapping paper etc etc

Amazing customer service and high quality are two of the core values of Velvet Paws.

The business will be run through the website as well as high-end markets around Brisbane, Gold Coast and Sunshine Coast.

Colors
eea4c8
ffffff
e34197

Requirements
Must have
• MUST BE FULLY OPERATIONAL ON COMPLETION. I own the domain name www.velvetpaws-example.com.au. Needs to be functioning on this domain with an operational online store using Payvora.
• Must also be mobile friendly.
• Pages:
• For your pup (shopping page)
• For your home (shopping page)
• For you (shopping page)
• Stationery
• Contact us
• I am open to better and more creative page names.
• MUST have an easy to operate back end that I can use to update products as and when required.

```html
<!DOCTYPE html>
<html lang="en">
<head>
<meta charset="utf-8">
<title>Velvet Paws – Checkout</title>
<link href="https://fonts.googleapis.com/css2?family=PT+Sans:ital,wght@0,400;0,700;1,400;1,700&family=Arimo:ital,wght@0,400;0,700;1,400&display=swap" rel="stylesheet">
<style>
  :root {
    --pink-soft: #eea4c8;
    --pink-band: #e294bb;
    --pink-strong: #e34197;
    --white: #ffffff;
    --page-bg: #e9e9e9;
    --panel-bg: #ececec;
    --slate: #575b78;
    --ink: #111111;
    --footer-dark: #232323;
    --footer-black: #050505;
    --rule: #b9b9b9;
  }
  * { box-sizing: border-box; margin: 0; padding: 0; }
  html, body { width: 1081px; height: 1200px; overflow: hidden; }
  body {
    position: relative;
    background: var(--page-bg);
    font-family: "Arimo", Arial, sans-serif;
  }
  .side-band {
    position: absolute; left: 0; top: 112px; width: 1081px; height: 37px;
    background: var(--pink-band);
  }
  .footer-floor {
    position: absolute; left: 0; top: 1010px; width: 1081px; height: 190px;
    background: var(--footer-black);
  }
  .shell {
    position: absolute; left: 202px; top: 0; width: 789px; height: 1200px;
    background: linear-gradient(#f6f6f6, var(--panel-bg) 140px);
    box-shadow: -3px 0 4px rgba(150,170,190,.35), 3px 0 4px rgba(150,170,190,.35);
  }
  .brand {
    position: absolute; left: 0; width: 789px; top: 60px;
    display: flex; justify-content: center; align-items: center; gap: 10px;
  }
  .brand-mark { width: 30px; height: 30px; background: var(--pink-strong); }
  .brand-name {
    font-family: "Arimo", Arial, sans-serif; font-weight: 700;
    font-size: 22px; letter-spacing: 1px; color: var(--slate);
  }
  .main-nav {
    position: absolute; left: 0; top: 132px; width: 789px; height: 37px;
    background: var(--pink-soft);
  }
  .main-nav a {
    position: absolute; top: 12px; font-size: 14px; color: var(--ink);
    text-decoration: none; line-height: 14px; white-space: nowrap;
  }
  .main-nav a.is-current { color: var(--white); }
  .cart-icon { position: absolute; left: 606px; top: 10px; }
  .checkout-tab {
    position: absolute; left: 39px; top: 202px; width: 145px; height: 27px;
    background: var(--pink-strong); color: var(--white);
    font-size: 14px; line-height: 27px; text-align: center;
  }
  .section-rule {
    position: absolute; left: 25px; top: 215px; width: 755px; height: 2px;
    background: var(--rule);
  }
  .cart-head {
    position: absolute; top: 254px; font-family: "PT Sans", sans-serif;
    font-weight: 700; font-size: 13px; color: var(--slate);
  }
  .line-item { position: absolute; left: 0; width: 789px; height: 120px; }
  .thumb {
    position: absolute; left: 54px; top: 0; width: 66px; height: 66px;
    background: var(--white);
  }
  .thumb i { position: absolute; inset: 6px; border-radius: 4px; }
  .item-title {
    position: absolute; left: 136px; top: 2px; font-family: "PT Sans", sans-serif;
    font-weight: 700; font-size: 12px; color: var(--slate);
  }
  .item-desc {
    position: absolute; left: 136px; top: 19px; width: 340px;
    font-family: "PT Sans", sans-serif; font-size: 10.6px; line-height: 15.6px;
    color: var(--slate);
  }
  .stepper { position: absolute; top: 24px; display: flex; align-items: center; gap: 3px; }
  .stepper .field {
    width: 36px; height: 22px; background: var(--white); margin-right: 2px;
    font-size: 10px; font-weight: 700; color: var(--slate);
    text-align: right; padding-right: 4px; line-height: 22px;
  }
  .price {
    position: absolute; left: 717px; top: 28px; font-family: "PT Sans", sans-serif;
    font-weight: 700; font-size: 14px; color: var(--pink-strong);
  }
  .delete-btn {
    position: absolute; left: 639px; top: 74px; width: 97px; height: 20px;
    background: var(--pink-strong); color: var(--white);
    font-family: "PT Sans", sans-serif; font-weight: 700; font-style: italic;
    font-size: 13px; line-height: 20px; text-align: center;
  }
  .proceed-btn {
    position: absolute; left: 602px; top: 912px; width: 186px; height: 27px;
    background: var(--pink-strong); color: var(--white);
    font-family: "Arimo", Arial, sans-serif; font-style: italic;
    font-size: 18px; line-height: 27px; text-align: center;
  }
  .site-footer {
    position: absolute; left: 0; top: 973px; width: 789px; height: 227px;
    background: var(--footer-dark);
  }
  .footer-band {
    position: absolute; left: 0; top: 18px; width: 789px; height: 28px;
    background: var(--pink-soft);
  }
  .footer-col { position: absolute; top: 61px; }
  .footer-col h4 {
    font-weight: 400; font-size: 12.5px; color: var(--pink-strong); margin-bottom: 9px;
  }
  .footer-col h4.light { color: var(--white); }
  .footer-col li { list-style: none; font-size: 12px; line-height: 15.6px; color: var(--white); }
  .social { position: absolute; left: 627px; top: 90px; display: flex; gap: 14px; }
  .social span {
    width: 37px; height: 37px; border-radius: 50%; background: var(--white);
    color: var(--footer-dark); font-size: 7.5px; font-weight: 700;
    display: flex; align-items: center; justify-content: center;
  }
  .copyright {
    position: absolute; left: 0; width: 789px; top: 186px; text-align: center;
    font-family: "Times New Roman", serif; font-size: 9px; color: var(--white);
  }
</style>
</head>
<body>
  <div class="side-band"></div>
  <div class="footer-floor"></div>

  <div class="shell">
    <header class="brand">
      <span class="brand-mark"></span>
      <span class="brand-name">VELVET PAWS</span>
    </header>

    <nav class="main-nav">
      <a class="is-current" style="left:20px">HOME</a>
      <a style="left:81px">PUPPIES</a>
      <a style="left:156px">MENS</a>
      <a style="left:214px">WOMENS</a>
      <a style="left:294px">STATIONERY</a>
      <a style="left:391px">CONTACT US</a>
      <a style="left:561px">CART</a>
      <svg class="cart-icon" width="16" height="16" viewBox="0 0 16 16" aria-hidden="true">
        <path d="M1 3h3l2 7h7l2-5H5" fill="none" stroke="#fff" stroke-width="1.6"/>
        <circle cx="7" cy="13" r="1.4" fill="#fff"/><circle cx="12" cy="13" r="1.4" fill="#fff"/>
      </svg>
      <a style="left:655px">LOGIN | SIGNUP</a>
    </nav>

    <div class="section-rule"></div>
    <div class="checkout-tab">CHECKOUT</div>

    <div class="cart-head" style="left:62px">Order no. 0017893547</div>
    <div class="cart-head" style="left:499px">Quantity</div>
    <div class="cart-head" style="left:616px">Size</div>
    <div class="cart-head" style="left:719px">Price</div>

    <article class="line-item" style="top:294px">
      <div class="thumb"><i role="img" aria-label="Photo of a hot dog costume for dogs" style="background:linear-gradient(#d9894a,#b0622c)"></i></div>
      <h3 class="item-title">Hot Dog Costume</h3>
      <p class="item-desc">Lorem ipsum dolor sit amet, consectetur adipiscing elit. Nullam venenatis cursus gravida. Suspendisse ut ligula tristique velit blandit blandit vel sit amet ipsum. Nam accumsan turpid id mauris fermentum</p>
      <div class="stepper" style="left:492px"><span class="field">1</span>
        <svg width="28" height="12" viewBox="0 0 28 12" aria-hidden="true"><g fill="none" stroke="#777"><circle cx="6" cy="6" r="4.5"/><circle cx="22" cy="6" r="4.5"/><path d="M3.5 6h5M6 3.5v5M19.5 6h5"/></g></svg></div>
      <div class="stepper" style="left:596px"><span class="field">7.5</span>
        <svg width="28" height="12" viewBox="0 0 28 12" aria-hidden="true"><g fill="none" stroke="#777"><circle cx="6" cy="6" r="4.5"/><circle cx="22" cy="6" r="4.5"/><path d="M3.5 6h5M6 3.5v5M19.5 6h5"/></g></svg></div>
      <span class="price">$8.50</span>
      <span class="delete-btn">Delete</span>
    </article>

    <article class="line-item" style="top:434px">
      <div class="thumb"><i role="img" aria-label="Photo of a hot dog costume for dogs" style="background:linear-gradient(#d9894a,#b0622c)"></i></div>
      <h3 class="item-title">Hot Dog Costumes</h3>
      <p class="item-desc">Lorem ipsum dolor sit amet, consectetur adipiscing elit. Nullam venenatis cursus gravida. Suspendisse ut ligula tristique velit blandit blandit vel sit amet ipsum. Nam accumsan turpid id mauris fermentum</p>
      <div class="stepper" style="left:492px"><span class="field">1</span>
        <svg width="28" height="12" viewBox="0 0 28 12" aria-hidden="true"><g fill="none" stroke="#777"><circle cx="6" cy="6" r="4.5"/><circle cx="22" cy="6" r="4.5"/><path d="M3.5 6h5M6 3.5v5M19.5 6h5"/></g></svg></div>
      <div class="stepper" style="left:596px"><span class="field">7.5</span>
        <svg width="28" height="12" viewBox="0 0 28 12" aria-hidden="true"><g fill="none" stroke="#777"><circle cx="6" cy="6" r="4.5"/><circle cx="22" cy="6" r="4.5"/><path d="M3.5 6h5M6 3.5v5M19.5 6h5"/></g></svg></div>
      <span class="price">$8.50</span>
      <span class="delete-btn">Delete</span>
    </article>

    <article class="line-item" style="top:575px">
      <div class="thumb"><i role="img" aria-label="Photo of a pepper shaped dog toy set" style="background:linear-gradient(90deg,#d8283a,#8a3f8e)"></i></div>
      <h3 class="item-title">Pepper Toy Set</h3>
      <p class="item-desc">Lorem ipsum dolor sit amet, consectetur adipiscing elit. Nullam venenatis cursus gravida. Suspendisse ut ligula tristique velit blandit blandit vel sit amet ipsum. Nam accumsan turpid id mauris fermentum</p>
      <div class="stepper" style="left:492px"><span class="field">1</span>
        <svg width="28" height="12" viewBox="0 0 28 12" aria-hidden="true"><g fill="none" stroke="#777"><circle cx="6" cy="6" r="4.5"/><circle cx="22" cy="6" r="4.5"/><path d="M3.5 6h5M6 3.5v5M19.5 6h5"/></g></svg></div>
      <div class="stepper" style="left:596px"><span class="field">7.5</span>
        <svg width="28" height="12" viewBox="0 0 28 12" aria-hidden="true"><g fill="none" stroke="#777"><circle cx="6" cy="6" r="4.5"/><circle cx="22" cy="6" r="4.5"/><path d="M3.5 6h5M6 3.5v5M19.5 6h5"/></g></svg></div>
      <span class="price">$8.50</span>
      <span class="delete-btn">Delete</span>
    </article>

    <article class="line-item" style="top:715px">
      <div class="thumb"><i role="img" aria-label="Photo of a striped dog jumper" style="background:linear-gradient(#c92a33,#e4e4e4 50%,#2a2a2a)"></i></div>
      <h3 class="item-title">Stripe Dog Jumper</h3>
      <p class="item-desc">Lorem ipsum dolor sit amet, consectetur adipiscing elit. Nullam venenatis cursus gravida. Suspendisse ut ligula tristique velit blandit blandit vel sit amet ipsum. Nam accumsan turpid id mauris fermentum</p>
      <div class="stepper" style="left:492px"><span class="field">1</span>
        <svg width="28" height="12" viewBox="0 0 28 12" aria-hidden="true"><g fill="none" stroke="#777"><circle cx="6" cy="6" r="4.5"/><circle cx="22" cy="6" r="4.5"/><path d="M3.5 6h5M6 3.5v5M19.5 6h5"/></g></svg></div>
      <div class="stepper" style="left:596px"><span class="field">7.5</span>
        <svg width="28" height="12" viewBox="0 0 28 12" aria-hidden="true"><g fill="none" stroke="#777"><circle cx="6" cy="6" r="4.5"/><circle cx="22" cy="6" r="4.5"/><path d="M3.5 6h5M6 3.5v5M19.5 6h5"/></g></svg></div>
      <span class="price">$8.50</span>
      <span class="delete-btn">Delete</span>
    </article>

    <span class="proceed-btn">Proceed to Checkout</span>

    <footer class="site-footer">
      <div class="footer-band"></div>
      <div class="footer-col" style="left:20px">
        <h4>LINKS</h4>
        <ul><li>Home</li><li>Mens</li><li>Womens</li><li>Stationary</li><li>Contact Us</li></ul>
      </div>
      <div class="footer-col" style="left:362px">
        <h4>ON SALE ITEMS</h4>
        <ul style="padding-left:10px"><li>Lorem ipsum</li><li>Lorem ipsum</li><li>Lorem ipsum</li><li>Lorem Ipsum</li></ul>
      </div>
      <div class="footer-col" style="left:624px">
        <h4 class="light">GET SOCIAL WITH US!</h4>
      </div>
      <div class="social"><span>Pawbook</span><span>Circlet</span><span>Chirper</span></div>
      <p class="copyright">© Copyright © 2011. Company name all rights reserved.</p>
    </footer>
  </div>
</body>
</html>
```